Brochure for medical doctor

I need a brochure for a medical doctor to promote his practice. The brochure should contain his picture, business information (use letterhead from attachment), and the following text:

- Now accepting PI cases on lien!
- Same and next business day appointments available for initial visits, pre-operative clearances, and all other medical needs

- Expedited medical reports sent quickly to your office

Medical

```html
<!DOCTYPE html>
<html lang="en">
<head>
<meta charset="utf-8">
<title>Willow Creek Medical Center – PI Cases Flyer</title>
<link rel="stylesheet" href="https://fonts.googleapis.com/css2?family=Barlow:wght@400;600;700&family=Poppins:wght@700&display=swap">
<style>
  :root{
    --navy:#3d4199;
    --sky:#7aa7d8;
    --pale:#eef2f9;
    --page-bg:#e6e9ef;
    --white:#ffffff;
  }
  *{margin:0;padding:0;box-sizing:border-box}
  html,body{width:1200px;height:1200px;overflow:hidden;background:var(--page-bg)}
  .stage{position:relative;width:1200px;height:1200px}
  .flyer{
    position:absolute;left:195px;top:25px;width:956px;height:1357px;
    transform:scale(0.8475);transform-origin:0 0;
    background:var(--white);overflow:hidden;
    font-family:"Barlow",sans-serif;color:var(--navy);
    box-shadow:0 18px 40px rgba(40,45,90,.25);
  }
  .backdrop{position:absolute;inset:0}
  .brand{position:absolute;left:82px;top:88px;display:flex;align-items:center;gap:18px}
  .brand-mark{width:30px;height:30px;background:var(--sky)}
  .brand-name{font-weight:700;font-size:31px;line-height:28px;color:var(--navy);letter-spacing:.3px}
  .brand-rule{position:absolute;left:82px;top:201px;width:495px;height:3px;
    background:linear-gradient(90deg,var(--navy),var(--sky) 60%,rgba(122,167,216,0))}
  .headline{position:absolute;left:80px;top:346px;font-family:"Poppins",sans-serif;font-weight:700;
    font-size:72px;line-height:61px;letter-spacing:-3px;color:var(--navy);text-transform:uppercase}
  .headline .accent{color:var(--sky)}
  .services{position:absolute;left:82px;top:668px;width:360px;list-style:none}
  .service{position:relative;display:flex;align-items:center;gap:24px}
  .service svg{flex:0 0 73px}
  .service p{font-size:22px;line-height:27px;letter-spacing:.2px}
  .service b{font-weight:700}
  .rule{margin:18px 0 18px 97px;width:131px;height:1px;background:#b9c6e4}
  .contact{position:absolute;left:82px;top:1168px;color:var(--white)}
  .contact h2{font-weight:700;font-size:35px;letter-spacing:.3px;line-height:40px}
  .contact h2 .accent{color:var(--sky)}
  .contact ul{list-style:none;margin-top:27px}
  .contact li{display:flex;align-items:center;gap:8px;font-size:20px;line-height:31px;letter-spacing:.3px}
  .contact b{font-weight:600}
</style>
</head>
<body>
<div class="stage">
  <article class="flyer">
    <svg class="backdrop" width="956" height="1357" viewBox="0 0 956 1357">
      <defs>
        <linearGradient id="lowerPale" x1="0" y1="0" x2="0" y2="1">
          <stop offset="0" stop-color="#ffffff"/>
          <stop offset="1" stop-color="#e9eef9"/>
        </linearGradient>
        <linearGradient id="cornerBlue" x1="0" y1="0" x2="0" y2="1">
          <stop offset="0" stop-color="#e4ebf8"/>
          <stop offset="1" stop-color="#86aee0"/>
        </linearGradient>
        <linearGradient id="portraitTone" x1="0" y1="0" x2="0.4" y2="1">
          <stop offset="0" stop-color="#e8e2de"/>
          <stop offset=".35" stop-color="#f1f3f7"/>
          <stop offset="1" stop-color="#e3e9f3"/>
        </linearGradient>
        <linearGradient id="contactBand" x1="0" y1="0" x2="1" y2="0">
          <stop offset="0" stop-color="#474ca6"/>
          <stop offset="1" stop-color="#80abdc"/>
        </linearGradient>
      </defs>
      <path d="M0,0 H470 C410,150 260,320 0,335 Z" fill="#eff3f9"/>
      <path d="M0,620 L520,1125 C560,1170 570,1260 555,1357 H0 Z" fill="url(#lowerPale)"/>
      <path d="M520,1125 L956,1125 L956,1357 L555,1357 C570,1260 560,1170 520,1125 Z" fill="url(#cornerBlue)"/>
      <path d="M956,180 L956,330 L720,560 L660,490 Z" fill="#7aa7d8"/>
      <path role="img" aria-label="Portrait of the doctor in a white coat with arms crossed"
            d="M820,70 C900,70 956,110 956,190 L956,1357 L940,1357 L600,1030
               C540,975 450,930 400,890 C380,830 395,740 450,680
               C520,600 600,560 690,500 C700,440 690,380 690,300
               C690,150 740,70 820,70 Z" fill="url(#portraitTone)"/>
      <path d="M600,1030 L940,1357" stroke="#ffffff" stroke-width="6"/>
      <path d="M0,1155 H530 C545,1175 552,1195 555,1220 H0 Z" fill="#3d4199"/>
      <path d="M0,1220 H555 C565,1270 563,1320 548,1357 H0 Z" fill="url(#contactBand)"/>
      <path d="M528,1152 C565,1200 575,1290 548,1357" fill="none" stroke="#ffffff" stroke-width="5"/>
    </svg>

    <div class="brand">
      <span class="brand-mark"></span>
      <div class="brand-name">WILLOW CREEK<br>MEDICAL<br>CENTER</div>
    </div>
    <div class="brand-rule"></div>

    <h1 class="headline">Now<br>Accepting<br><span class="accent">PI Cases</span><br>On Lien!</h1>

    <ul class="services">
      <li class="service">
        <svg width="73" height="64" viewBox="0 0 73 64" fill="none" stroke="#3d4199" stroke-width="2.5">
          <rect x="4" y="8" width="54" height="48" rx="3"/>
          <path d="M4,18 H58" stroke-width="4"/>
          <path d="M16,3 V12 M46,3 V12"/>
          <rect x="12" y="26" width="7" height="6" fill="#3d4199"/><rect x="24" y="26" width="7" height="6" fill="#3d4199"/><rect x="36" y="26" width="7" height="6" fill="#3d4199"/>
          <rect x="12" y="37" width="7" height="6" fill="#3d4199"/><rect x="24" y="37" width="7" height="6" fill="#3d4199"/>
          <circle cx="56" cy="48" r="13" fill="#fff" stroke="#7aa7d8"/>
          <path d="M56,41 V48 H62" stroke="#7aa7d8"/>
        </svg>
        <p>Same and next business<br>day appointments<br><b>available</b> for initial visits</p>
      </li>
      <li class="rule"></li>
      <li class="service">
        <svg width="73" height="64" viewBox="0 0 73 64" fill="none" stroke="#3d4199" stroke-width="2">
          <rect x="6" y="2" width="40" height="40" rx="2"/>
          <path d="M12,24 H20 L24,16 L29,30 L33,22 H40" stroke="#7aa7d8"/>
          <rect x="30" y="22" width="34" height="40" rx="2" fill="#fff"/>
          <path d="M36,32 H42 M46,32 H58 M36,40 H42 M46,40 H58 M36,48 H42"/>
          <path d="M47,50 L51,54 L58,46" stroke="#7aa7d8"/>
        </svg>
        <p>Pre-operative<br><b>clearances</b></p>
      </li>
      <li class="rule"></li>
      <li class="service">
        <svg width="73" height="64" viewBox="0 0 73 64" fill="none" stroke="#3d4199" stroke-width="2">
          <circle cx="18" cy="14" r="12"/>
          <path d="M18,8 V14 H24" stroke="#7aa7d8"/>
          <path d="M22,26 L26,36"/>
          <rect x="20" y="30" width="40" height="32" rx="2" fill="#fff" stroke="#7aa7d8"/>
          <path d="M35,38 H45 V43 H50 V51 H45 V56 H35 V51 H30 V43 H35 Z"/>
        </svg>
        <p><b>Other</b> medical needs</p>
      </li>
      <li class="rule"></li>
      <li class="service">
        <svg width="73" height="64" viewBox="0 0 73 64" fill="none" stroke="#3d4199" stroke-width="2.5">
          <path d="M2,24 H22 M8,30 H22 M0,36 H22 M10,42 H22"/>
          <rect x="20" y="18" width="30" height="26" fill="#7aa7d8" stroke="#3d4199"/>
          <path d="M50,26 H62 L70,36 V44 H50 Z"/>
          <circle cx="32" cy="46" r="5" fill="#fff"/><circle cx="62" cy="46" r="5" fill="#fff"/>
        </svg>
        <p>Expedited medical<br>reports <b>sent quickly</b><br>to your office</p>
      </li>
    </ul>

    <section class="contact">
      <h2><span class="accent">CONTACT</span> US</h2>
      <ul>
        <li>
          <svg width="20" height="22" viewBox="0 0 20 22"><path d="M10,1 C5,1 2,4.5 2,8.5 C2,14 10,21 10,21 C10,21 18,14 18,8.5 C18,4.5 15,1 10,1 Z" fill="#fff"/><circle cx="10" cy="8.5" r="3" fill="#5a6cb6"/></svg>
          4150 Maple Grove Ave. Lakeview, CA, 90000
        </li>
        <li>
          <svg width="20" height="22" viewBox="0 0 20 22" fill="none" stroke="#fff" stroke-width="2"><path d="M5,2 L8,7 L6,9 C7,12 9,14 12,16 L14,14 L19,17 L17,20 C10,20 2,12 2,5 Z"/></svg>
          <span><b>Tel:</b> (555) 014-2200</span>
        </li>
        <li>
          <svg width="20" height="22" viewBox="0 0 20 22" fill="none" stroke="#fff" stroke-width="1.8"><rect x="5" y="2" width="10" height="6"/><rect x="1" y="8" width="18" height="9" rx="2"/><rect x="5" y="13" width="10" height="7" fill="#7197d2"/></svg>
          <span><b>Fax:</b> (555) 014-2207</span>
        </li>
      </ul>
    </section>
  </article>
</div>
</body>
</html>
```